Mini Market Tavo Business Presentation Cards

We need presentation cards with a logo we already own designed at this website as well. We need the printing, delivery and sleek, modem design in harmony with our previous logo design.

Target Market(s)

Low, med and High income class.

Industry/Entity Type

Grocery Store

Contact Information for Business Card

Business logo (Mini Market Tavo), name: Esteban L. Morales/Lidia M. Paz/ Hugo Paz (those are the names for the different cards),
Address: Col. Lomas del Viento, carretera a Tela a 200mts del Centro Comunal. Puerto Cortés, Honduras.
Email: minimarkettavo@correo-ejemplo.hn
Teléfono: (504) 9731-5064

Font styles to use
Serif
Sans Serif

Requirements
Must have
• Business logo (Mini Market Tavo), person name, department,
• Address, phone number, email address.

```html
<!DOCTYPE html>
<html lang="es">
<head>
<meta charset="utf-8">
<title>Mini Market Tavo — Tarjeta de presentación</title>
<link rel="stylesheet" href="https://fonts.googleapis.com/css2?family=Archivo+Black&family=Pathway+Gothic+One&display=swap">
<style>
  :root {
    --brand-red: #d94a35;
    --mark-neutral: #d9d9d9;
    --ink: #111111;
    --paper: #ffffff;
  }
  * { margin: 0; padding: 0; box-sizing: border-box; }
  html, body {
    width: 1200px;
    height: 686px;
    overflow: hidden;
    background: var(--paper);
  }
  .business-card {
    position: relative;
    width: 1200px;
    height: 686px;
    background: var(--paper);
    color: var(--ink);
  }
  .brand {
    position: absolute;
    left: 400px;
    top: 92px;
    width: 742px;
    height: 220px;
    display: flex;
    align-items: center;
    justify-content: flex-end;
    gap: 36px;
  }
  .brand-name {
    font-family: "Pathway Gothic One", "Arial Narrow", sans-serif;
    font-weight: 400;
    font-size: 84px;
    line-height: 1;
    color: var(--brand-red);
    white-space: nowrap;
  }
  .brand-dot {
    flex: 0 0 auto;
    width: 200px;
    height: 200px;
  }
  .person-name {
    position: absolute;
    left: 56px;
    top: 362px;
    font-family: "Archivo Black", "Arial Black", sans-serif;
    font-size: 56px;
    line-height: 1;
    letter-spacing: 0.5px;
  }
  .address, .contact {
    position: absolute;
    font-family: "Pathway Gothic One", "Arial Narrow", sans-serif;
    font-size: 37px;
    line-height: 49px;
    font-style: normal;
    white-space: nowrap;
  }
  .address {
    left: 58px;
    top: 441px;
  }
  .contact {
    right: 56px;
    top: 540px;
    text-align: left;
  }
  .address span, .contact span { display: block; }
</style>
</head>
<body>
  <main class="business-card">
    <div class="brand">
      <span class="brand-name">Mini Market Tavo</span>
      <svg class="brand-dot" viewBox="0 0 200 200" aria-hidden="true">
        <circle cx="100" cy="100" r="100" fill="var(--mark-neutral)"/>
      </svg>
    </div>

    <h1 class="person-name">Lidia M. Paz</h1>

    <address class="address">
      <span>Col. Lomas del Viento</span>
      <span>Carretera a Tela a 200mts del Centro Comunal</span>
      <span>Puerto Cortés</span>
      <span>Honduras</span>
    </address>

    <address class="contact">
      <span class="phone">(504) 9731-5064</span>
      <span class="email">minimarkettavo@correo-ejemplo.hn</span>
    </address>
  </main>
</body>
</html>
```